Design Cloud for Core Values & Attributes

See Image Example Below "Word Cloud" this is what we would like this to look like.
The second image is all of the Core Value and Attributes I will list below.
CORE VALUES need to be the bigger words (based off the image I sent) Capitalized, BOLD, Navy
Independence, Capitalism, Trust, Fun, Safety, Growth
ATTRIBUTES need to be the smaller words, lower case, non-bold, lighter blue mixed in (based off the image I sent):
Humility, Consistency, Open Mindedness, Curiosity, Selflessness, Caring, Conscientiousness, Honorable, Cunning, Competitive, Compartmentalization, Innovative, Perseverance, Authenticity, Decisiveness, Self-efficacy, Accountability, Generosity, Humor, Optimism, Resilience, Inclusive, Insouciance to what others think, Courage, Decisive, Curious, Integrity

```html
<!DOCTYPE html>
<html lang="en">
<head>
<meta charset="utf-8">
<title>Core Values &amp; Attributes</title>
<link rel="stylesheet" href="https://fonts.googleapis.com/css2?family=Roboto+Condensed:wght@300;400;700&display=swap">
<style>
  :root {
    --paper: #ffffff;
    --cloud: #deeef8;
    --navy: #1b3a8f;
    --blue-mid: #2c68b8;
    --blue-light: #5d98d2;
    --teal: #2fa7bf;
    --rule: #8ab6dc;
  }
  html, body {
    margin: 0;
    width: 1200px;
    height: 941px;
    overflow: hidden;
    background: var(--paper);
  }
  .value-cloud {
    display: block;
    width: 1200px;
    height: 941px;
    font-family: "Roboto Condensed", "Arial Narrow", sans-serif;
  }
  .cloud-shape { fill: var(--cloud); }
  .rule { stroke: var(--rule); stroke-width: 1.5; }
  .core { fill: var(--navy); font-weight: 700; font-size: 60px; text-anchor: middle; }
  .attr-line { font-size: 22px; text-anchor: middle; }
  .attr-mid { fill: var(--blue-mid); font-weight: 400; }
  .attr-light { fill: var(--blue-light); font-weight: 300; }
  .attr-teal { fill: var(--teal); font-weight: 400; }
  .section-label { fill: var(--blue-mid); font-weight: 400; font-size: 38px; text-anchor: middle; }
</style>
</head>
<body>
<svg class="value-cloud" viewBox="0 0 1200 941" xmlns="http://www.w3.org/2000/svg" role="img" aria-label="Cloud of core values with their attributes">
  <path class="cloud-shape" d="M 190 800
    C 90 800 70 690 130 650
    C 80 570 120 460 210 450
    C 200 330 330 270 430 300
    C 480 190 700 180 760 290
    C 870 250 1000 300 1010 420
    C 1110 430 1130 560 1070 620
    C 1130 700 1080 800 990 800 Z"/>

  <!-- Capitalism -->
  <text class="attr-line" x="375" y="355"><tspan class="attr-teal">Cunning</tspan><tspan class="attr-light" dx="14">Competitive</tspan></text>
  <text class="core" x="375" y="420" textLength="290" lengthAdjust="spacingAndGlyphs">CAPITALISM</text>
  <text class="attr-line attr-mid" x="375" y="462" font-size="26">Perseverance</text>
  <text class="attr-line attr-light" x="375" y="492">Compartmentalization</text>

  <!-- Safety -->
  <text class="attr-line attr-light" x="650" y="322">Courage</text>
  <text class="attr-line" x="650" y="355"><tspan class="attr-teal">Integrity</tspan><tspan class="attr-mid" dx="14">Decisive</tspan></text>
  <text class="core" x="650" y="420" textLength="190" lengthAdjust="spacingAndGlyphs">SAFETY</text>
  <text class="attr-line attr-teal" x="650" y="462" font-size="26">Accountability</text>
  <text class="attr-line" x="650" y="492"><tspan class="attr-mid">Humility</tspan><tspan class="attr-light" dx="14">Curious</tspan></text>

  <!-- Growth -->
  <text class="attr-line attr-mid" x="880" y="355">Innovative</text>
  <text class="core" x="880" y="420" textLength="200" lengthAdjust="spacingAndGlyphs">GROWTH</text>
  <text class="attr-line" x="880" y="462"><tspan class="attr-teal">Curiosity</tspan><tspan class="attr-light" dx="14">Caring</tspan></text>
  <text class="attr-line" x="880" y="492"><tspan class="attr-mid">Honorable</tspan><tspan class="attr-light" dx="14">Generosity</tspan></text>

  <!-- Trust -->
  <text class="attr-line" x="290" y="555"><tspan class="attr-mid">Resilience</tspan><tspan class="attr-light" dx="14">Consistency</tspan></text>
  <text class="attr-line attr-teal" x="290" y="585">Conscientiousness</text>
  <text class="core" x="290" y="660" textLength="190" lengthAdjust="spacingAndGlyphs">TRUST</text>
  <text class="attr-line attr-teal" x="290" y="700" font-size="26">Open Mindedness</text>
  <text class="attr-line" x="290" y="730"><tspan class="attr-mid">Caring</tspan><tspan class="attr-light" dx="14">Humility</tspan></text>

  <!-- Independence -->
  <text class="attr-line" x="610" y="555"><tspan class="attr-teal">Authenticity</tspan><tspan class="attr-mid" dx="14">Self-efficacy</tspan></text>
  <text class="attr-line attr-light" x="610" y="585">Decisiveness</text>
  <text class="core" x="610" y="660" textLength="370" lengthAdjust="spacingAndGlyphs">INDEPENDENCE</text>
  <text class="attr-line" x="610" y="700"><tspan class="attr-teal">Selflessness</tspan><tspan class="attr-light" dx="14">Curiosity</tspan></text>
  <line class="rule" x1="480" y1="722" x2="740" y2="722"/>
  <text class="section-label" x="610" y="765">Attributes</text>

  <!-- Fun -->
  <text class="attr-line" x="920" y="555"><tspan class="attr-light">Humor</tspan><tspan class="attr-mid" dx="14">Optimism</tspan></text>
  <text class="attr-line attr-teal" x="920" y="585">Inclusive</text>
  <text class="core" x="920" y="660" textLength="120" lengthAdjust="spacingAndGlyphs">FUN</text>
  <text class="attr-line attr-teal" x="920" y="700" font-size="19">Insouciance to What Others Think</text>
  <text class="attr-line attr-mid" x="920" y="730">Humility</text>
</svg>
</body>
</html>
```